Web design for Modeling agency

We are looking for re-designing our modeling agency website.
Current website: lunafaces.com our competitor: KTRfaces.com
http://brisaface.fr/
https://www.corvelmanagement.com/models/
https://www.hedwig-faces.de
https://www.rustmanagement.co.uk
https://www.quorbfaces.com
https://www.harborlightfaces.com

Target Market(s)

modeling agency

Industry/Entity Type

modeling agency

Number of Pages Required

5+ page

Font styles to use
Other font styles liked:
• base on logo guidline

Requirements
Nice to have
• current website: lunafaces.com our competitor: KTRfaces.com

```html
<!DOCTYPE html>
<html lang="en">
<head>
<meta charset="utf-8">
<title>Luna Faces</title>
<link href="https://fonts.googleapis.com/css2?family=Poppins:wght@300;400;500;600&display=swap" rel="stylesheet">
<style>
:root{
  --accent:#bd9d86;
  --accent-dark:#9c7b66;
  --text-muted:#a9a9a9;
  --card-bg:#f8f8f8;
  --line:#e6e6e6;
  --white:#ffffff;
  --hero-dark:#3a2519;
  --hero-mid:#5e3f2c;
}
*{margin:0;padding:0;box-sizing:border-box}
html,body{width:1200px;height:821px;overflow:hidden;background:var(--white);font-family:"Poppins",sans-serif}
.page{position:relative;width:1200px;height:821px}
.site-header{position:absolute;left:0;top:0;width:1200px;height:44px;border-bottom:1px solid var(--line)}
.main-nav a{position:absolute;top:16px;font-size:11px;font-weight:300;color:var(--text-muted);text-decoration:none}
.main-nav a.active{color:var(--accent);font-weight:400}
.main-nav a.active::after{content:"";position:absolute;left:1px;right:0;top:26px;height:2px;background:var(--accent)}
.search{position:absolute;left:797px;top:11px;width:169px;height:22px;border:1px solid #cfcfcf;border-radius:11px;padding-left:15px;font-size:10.5px;font-weight:300;color:#b5b5b5;line-height:20px}
.search svg{position:absolute;right:12px;top:4px}
.menu-btn{position:absolute;left:1148px;top:0;width:52px;height:44px;background:var(--accent)}
.menu-btn span{position:absolute;left:14px;width:24px;height:1.5px;background:var(--white)}
.hero{position:absolute;left:234px;top:64px;width:732px;height:232px;border-radius:19px;overflow:hidden;background:linear-gradient(90deg,#2d1c13 0%,var(--hero-mid) 45%,#4a2e1f 75%,var(--hero-dark) 100%)}
.hero-photo{position:absolute;right:0;top:0;width:300px;height:232px;background:radial-gradient(ellipse at 60% 45%,#b07a5e 0%,#6a4130 55%,rgba(58,37,25,0) 100%)}
.brand{position:absolute;left:0;width:327px;text-align:center;color:var(--white);font-weight:300}
.brand-name{top:50px;font-size:40px;letter-spacing:2px;line-height:1.3}
.brand-sub{top:110px;font-size:20px;letter-spacing:1px}
.hero-cta{position:absolute;left:75px;top:151px;width:175px;height:29px;border-radius:15px;background:var(--white);color:var(--accent);font-size:11px;font-weight:300;text-align:center;line-height:29px}
.show-card{position:absolute;width:163px;height:74px;border-radius:12px;background:var(--card-bg)}
.show-card.featured{background:var(--accent);box-shadow:0 4px 10px rgba(0,0,0,.18)}
.show-city{position:absolute;left:22px;top:21px;font-size:12.5px;font-weight:600;color:var(--accent)}
.show-mag{position:absolute;left:22px;top:39px;font-size:9.5px;font-weight:400;color:var(--text-muted)}
.show-date{position:absolute;left:145px;top:17px;writing-mode:vertical-rl;font-size:6.5px;font-weight:600;color:var(--accent)}
.featured .show-city,.featured .show-mag,.featured .show-date{color:var(--white)}
.newsletter{position:absolute;left:234px;top:579px;width:732px;height:150px;border-radius:19px;background:var(--accent)}
.newsletter h2{position:absolute;top:32px;width:100%;text-align:center;font-size:15.5px;font-weight:400;color:var(--white)}
.field{position:absolute;top:70px;width:178px;height:36px;border-radius:18px;background:var(--white);padding-left:16px;line-height:36px;font-size:10.5px;font-weight:300;color:#8d8d8d}
.subscribe-btn{position:absolute;left:488px;top:70px;width:123px;height:36px;border-radius:18px;background:var(--accent-dark);color:var(--white);font-size:10.5px;text-align:center;line-height:36px}
.address{position:absolute;top:744px;width:1200px;text-align:center;font-size:13px;font-weight:300;color:var(--text-muted)}
.footer{position:absolute;left:0;top:772px;width:1200px;height:49px;border-top:1px solid var(--line)}
.contact{position:absolute;top:13px;display:flex;align-items:center;gap:6px;font-size:12px;font-weight:300;color:var(--text-muted)}
.contact-icon{width:14px;height:14px;border-radius:50%;background:var(--accent);display:flex;align-items:center;justify-content:center}
</style>
</head>
<body>
<div class="page">
  <header class="site-header">
    <nav class="main-nav">
      <a class="active" href="#" style="left:234px">Women’s</a>
      <a href="#" style="left:310px">Men’s</a>
      <a href="#" style="left:366px">Artists</a>
      <a href="#" style="left:425px">Social</a>
      <a href="#" style="left:485px">Contact</a>
    </nav>
    <div class="search">Search
      <svg width="13" height="13" viewBox="0 0 13 13"><circle cx="5.5" cy="5.5" r="4.5" fill="none" stroke="#b5b5b5" stroke-width="1.2"/><line x1="9" y1="9" x2="12.5" y2="12.5" stroke="#b5b5b5" stroke-width="1.2"/></svg>
    </div>
    <div class="menu-btn"><span style="top:14px"></span><span style="top:21px"></span><span style="top:28px"></span></div>
  </header>

  <section class="hero">
    <div class="hero-photo" role="img" aria-label="Portrait photograph of a model wearing jewellery"></div>
    <div class="brand brand-name">LUNA</div>
    <div class="brand brand-sub">FACES</div>
    <div class="hero-cta">Show Us Your Style!</div>
  </section>

  <section class="shows">
    <div class="show-card" style="left:234px;top:349px"><div class="show-city">LONDON</div><div class="show-mag">Hazel Magazine</div><div class="show-date">SEP 16, 2021</div></div>
    <div class="show-card featured" style="left:422px;top:349px"><div class="show-city">PARIS</div><div class="show-mag">Hazel Magazine</div><div class="show-date">SEP 16, 2021</div></div>
    <div class="show-card" style="left:612px;top:349px"><div class="show-city">ISTANBUL</div><div class="show-mag">Gravia International</div><div class="show-date">SEP 16, 2021</div></div>
    <div class="show-card" style="left:801px;top:349px"><div class="show-city">MILAN</div><div class="show-mag">Velour Ukraine</div><div class="show-date">SEP 16, 2021</div></div>
    <div class="show-card" style="left:234px;top:456px"><div class="show-city">ATHENS</div><div class="show-mag">Velour Italia</div><div class="show-date">SEP 16, 2021</div></div>
    <div class="show-card" style="left:422px;top:456px"><div class="show-city">DUBAI</div><div class="show-mag">Nuvelle Magazine</div><div class="show-date">SEP 16, 2021</div></div>
    <div class="show-card" style="left:612px;top:456px"><div class="show-city">LOS ANGELES</div><div class="show-mag">Hazel Magazine</div><div class="show-date">SEP 16, 2021</div></div>
    <div class="show-card" style="left:801px;top:456px"><div class="show-city">CHICAGO</div><div class="show-mag">Prism Magazine</div><div class="show-date">SEP 16, 2021</div></div>
  </section>

  <section class="newsletter">
    <h2>Subscribe Our Newsleter &amp; Join Us</h2>
    <div class="field" style="left:120px">Name</div>
    <div class="field" style="left:305px">Email</div>
    <div class="subscribe-btn">Subscribe</div>
  </section>

  <p class="address">Unit 14, Floor 9th, A Blok, Meridyen Plaza, Lale Street, Kadikoy, Istanbul, Turkey</p>

  <footer class="footer">
    <div class="contact" style="left:382px">
      <span class="contact-icon"><svg width="8" height="8" viewBox="0 0 8 8"><path d="M1.5 0.8 L3 2.5 L2.3 3.3 Q3.2 4.9 4.7 5.7 L5.5 5 L7.2 6.5 L6.3 7.4 Q2.5 7 0.6 1.7 Z" fill="#fff"/></svg></span>+44 700 555 01 23</div>
    <div class="contact" style="left:521px">
      <span class="contact-icon"><svg width="8" height="8" viewBox="0 0 8 8"><rect x="2.2" y="0.5" width="3.6" height="7" rx="0.7" fill="none" stroke="#fff" stroke-width="0.9"/></svg></span>+90 500 555 44 88</div>
    <div class="contact" style="left:651px">
      <span class="contact-icon"><svg width="8" height="8" viewBox="0 0 8 8"><rect x="0.5" y="1.5" width="7" height="5" fill="none" stroke="#fff" stroke-width="0.9"/><path d="M0.5 1.8 L4 4.5 L7.5 1.8" fill="none" stroke="#fff" stroke-width="0.9"/></svg></span>booker@lunafaces.com</div>
  </footer>
</div>
</body>
</html>
```